Business card design for international hub site

I need a business card design with the logo attached. Although the site is for the teenage audience (it is about the high school graduation ball, the Prom), the business card is for professional use to be given to professional contacts (B2B), such as suppliers and partners, so it needs to look professional (but also girly, glamours and clean).

Target Market(s)

B2B

Industry/Entity Type

Media

Colors
eea4c8
f9d9e8
e667a6
9d9d9d
1b1b1b

Requirements
Must have
• Space for Name, Tile, Address, Phone, email and website.
Should not have
• Photo

```html
<!DOCTYPE html>
<html lang="en">
<head>
<meta charset="utf-8">
<title>Gala Whirl — Business Card</title>
<link href="https://fonts.googleapis.com/css2?family=EB+Garamond:wght@400;600&family=Pinyon+Script&display=swap" rel="stylesheet">
<style>
  :root {
    --page-bg: #ececec;
    --pink: #fd4389;
    --pink-deep: #e83279;
    --pink-soft: #f0609e;
    --charcoal: #2b2b2b;
    --charcoal-deep: #1f1f1f;
    --white: #ffffff;
    --text-light: #eeeeee;
  }
  * { margin: 0; padding: 0; box-sizing: border-box; }
  html, body { width: 1200px; height: 586px; overflow: hidden; }
  body {
    background: var(--page-bg);
    position: relative;
    font-family: "EB Garamond", Georgia, serif;
  }
  .card {
    position: absolute;
    top: 126px;
    width: 502px;
    height: 301px;
    overflow: hidden;
  }
  .card--front { left: 65px; }
  .card--back { left: 608px; }
  .card__texture {
    position: absolute;
    inset: 0;
  }
  .card--front .card__texture {
    background: linear-gradient(135deg, var(--pink) 0%, var(--pink-deep) 45%, var(--pink) 70%, var(--pink-deep) 100%);
  }
  .card--back .card__texture {
    background: linear-gradient(135deg, var(--charcoal) 0%, var(--charcoal-deep) 50%, var(--charcoal) 100%);
  }
  .brand-name {
    position: absolute;
    left: 0; right: 0;
    top: 108px;
    text-align: center;
    color: var(--white);
    font-size: 54px;
    font-weight: 400;
    line-height: 1;
  }
  .website {
    position: absolute;
    left: 0; right: 0;
    top: 258px;
    text-align: center;
    color: var(--white);
    font-size: 12px;
    font-weight: 600;
    letter-spacing: 3.2px;
  }
  .person-name {
    position: absolute;
    left: 20px;
    width: 230px;
    top: 134px;
    text-align: center;
    color: var(--white);
    font-family: "Pinyon Script", cursive;
    font-size: 30px;
    line-height: 1.2;
  }
  .divider {
    position: absolute;
    left: 251px;
    top: 83px;
    width: 2px;
    height: 140px;
    background: linear-gradient(to bottom, transparent, var(--pink) 40%, var(--pink) 60%, transparent);
  }
  .contact-list {
    position: absolute;
    left: 284px;
    top: 122px;
    list-style: none;
  }
  .contact-list li {
    display: flex;
    align-items: center;
    height: 24.5px;
    color: var(--text-light);
    font-size: 13px;
  }
  .contact-list svg {
    width: 13px;
    height: 11px;
    margin-right: 7px;
    fill: var(--pink-soft);
  }
  .address {
    position: absolute;
    left: 0; right: 0;
    top: 270px;
    text-align: center;
    color: var(--pink-soft);
    font-size: 14px;
    font-weight: 600;
  }
</style>
</head>
<body>
  <section class="card card--front">
    <div class="card__texture" role="img" aria-label="Faceted low-poly pink background texture"></div>
    <div class="brand-name">Gala Whirl</div>
    <div class="website">www.galawhirl.com</div>
  </section>

  <section class="card card--back">
    <div class="card__texture" role="img" aria-label="Faceted low-poly charcoal background texture"></div>
    <div class="person-name">Mara Linwood</div>
    <div class="divider"></div>
    <ul class="contact-list">
      <li>
        <svg viewBox="0 0 16 14" aria-hidden="true"><path d="M1 5c0-2 3-3 7-3s7 1 7 3v1.5h-3.5V5H4.5v1.5H1z"/><path d="M4 7h8l2 6H2z"/></svg>
        +44 (0)1632 960418
      </li>
      <li>
        <svg viewBox="0 0 16 14" aria-hidden="true"><rect x="4" y="0" width="8" height="3"/><rect x="0" y="4" width="16" height="6" rx="1"/><rect x="4" y="8" width="8" height="6"/></svg>
        (555) 014-2290
      </li>
      <li>
        <svg viewBox="0 0 16 12" aria-hidden="true"><path d="M0 0h16v1L8 7 0 1z"/><path d="M0 3l8 6 8-6v9H0z"/></svg>
        mara@galawhirl.com
      </li>
    </ul>
    <div class="address">Elm Court, Hollow Bridge, YX4 2QT</div>
  </section>
</body>
</html>
```